Real Estate investment company needs billboard designs

This is our website: https://velmarkpropertygroup.com/
We are looking for some billboard concepts that uses our CEO in the design. I have attached some images and 1 billboard design that someone in our industry uses, but we don't want it exactly like his.

Industry/Entity Type

real estate

Colors

Designer to choose colors to be used in the design.

Requirements
Must have
• Company colors from websiute

```html
<!DOCTYPE html>
<html lang="en">
<head>
<meta charset="utf-8">
<title>Velmark Property Group Billboard</title>
<link href="https://fonts.googleapis.com/css2?family=Oswald:wght@500;600;700&family=Roboto:wght@900&display=swap" rel="stylesheet">
<style>
  :root {
    --navy: #1b1c43;
    --red: #e32528;
    --white: #ffffff;
    --backdrop: #7d7e83;
    --shirt-light: #9fb3cf;
    --shirt-dark: #5d6f93;
  }
  * { margin: 0; padding: 0; box-sizing: border-box; }
  html, body {
    width: 1200px; height: 762px; overflow: hidden;
    background: var(--backdrop);
  }
  .billboard {
    position: absolute; left: 30px; top: 118px;
    width: 1140px; height: 526px;
    background: var(--white);
    overflow: hidden;
    box-shadow: 0 6px 18px rgba(0,0,0,.25);
    font-family: 'Oswald', sans-serif;
  }
  .lower-band {
    position: absolute; left: 0; right: 0; top: 319px; bottom: 0;
    background: var(--navy);
  }
  .brand-name {
    position: absolute; left: 42px; top: 34px; width: 405px;
    color: var(--navy); font-weight: 700; text-transform: uppercase;
    text-align: right;
  }
  .brand-name .main { display: block; font-size: 104px; line-height: 104px; letter-spacing: 2px; text-align: left; }
  .brand-name .sub { display: block; font-size: 26px; line-height: 30px; letter-spacing: 1px; }
  .website {
    position: absolute; left: 42px; top: 198px; width: 405px;
    color: var(--navy); font-weight: 600; font-size: 36px; line-height: 52px;
    text-decoration: none; letter-spacing: -0.3px;
  }
  .house-photo {
    position: absolute; left: 73px; top: 261px; width: 344px; height: 177px;
    border-radius: 20px;
    background: linear-gradient(180deg, #3e7fd0 0%, #9fc2e6 38%, #b8a98a 60%, #7fb34a 100%);
  }
  .phone {
    position: absolute; left: 100px; top: 444px; width: 290px;
    color: var(--white); font-family: 'Roboto', sans-serif; font-weight: 900;
    font-size: 40px; line-height: 48px; letter-spacing: 1px; text-align: center;
  }
  .ceo-portrait {
    position: absolute; left: 472px; top: 10px; width: 327px; height: 450px;
    border-radius: 120px 120px 30px 30px;
    background: linear-gradient(180deg, #e8cbb8 0%, #e8cbb8 22%, var(--shirt-light) 32%, var(--shirt-dark) 80%, rgba(27,28,67,0) 100%);
  }
  .divider-bar {
    position: absolute; left: 450px; top: 461px; width: 352px; height: 13px;
    border-radius: 7px; background: var(--white);
  }
  .headline {
    position: absolute; right: 41px; top: 14px;
    text-align: right; font-weight: 700; text-transform: uppercase;
    font-size: 106px; line-height: 91px; letter-spacing: -1px;
  }
  .headline span { display: block; }
  .headline .navy { color: var(--navy); }
  .headline .red { color: var(--red); }
  .steps {
    position: absolute; right: 42px; top: 343px; list-style: none;
  }
  .steps li {
    display: flex; justify-content: flex-end; align-items: center;
    height: 52px; color: var(--white); font-weight: 600; font-size: 25px;
  }
  .steps svg { width: 36px; height: 36px; margin-left: 18px; fill: var(--red); }
</style>
</head>
<body>
  <div class="billboard">
    <div class="lower-band"></div>

    <div class="brand-name">
      <span class="main">Velmark</span>
      <span class="sub">Property Group</span>
    </div>
    <a class="website" href="https://velmarkpropertygroup.com/">velmarkpropertygroup.com</a>

    <div class="house-photo" role="img" aria-label="Photo of a two-storey suburban house with a garage and green lawn"></div>
    <div class="phone">865-555-0142</div>

    <div class="ceo-portrait" role="img" aria-label="Photo of the company CEO in a light blue denim shirt with arms crossed"></div>
    <div class="divider-bar"></div>

    <h1 class="headline">
      <span class="navy">We Buy</span>
      <span class="red">Houses</span>
      <span class="navy">Fast!</span>
    </h1>

    <ul class="steps">
      <li>Reach Out
        <svg viewBox="0 0 36 36" aria-hidden="true"><path d="M18 3 L2 17 L6 17 L6 33 L15 33 L15 24 L21 24 L21 33 L30 33 L30 17 L34 17 L27 11 L27 5 L24 5 L24 8.5 Z"/></svg>
      </li>
      <li>Schedule a Visit
        <svg viewBox="0 0 36 36" aria-hidden="true"><circle cx="25" cy="15" r="9"/><rect x="23" y="3" width="4" height="4"/><rect x="1" y="22" width="5" height="10"/><path d="M7 23 C12 21 16 22 20 25 L28 24 C31 24 31 28 28 28 L17 30 L7 30 Z"/><text x="25" y="19" font-size="11" font-family="Oswald, sans-serif" font-weight="700" fill="#1b1c43" text-anchor="middle">$</text></svg>
      </li>
      <li>Accept &amp; Get Paid
        <svg viewBox="0 0 36 36" aria-hidden="true"><rect x="3" y="5" width="30" height="29" rx="3"/><rect x="9" y="1" width="4" height="8" rx="1" fill="#ffffff"/><rect x="23" y="1" width="4" height="8" rx="1" fill="#ffffff"/><rect x="3" y="11" width="30" height="2" fill="#1b1c43"/><path d="M11 22 L16 27 L26 17" stroke="#1b1c43" stroke-width="3" fill="none"/></svg>
      </li>
    </ul>
  </div>
</body>
</html>
```